Polystyrene Environmental Synopsis

We need a fact sheet for quick reference that groups information units and has a simple but engaging visual presentation of the text and various infographics. We are a trade association representing polystyrene foam manufacturers and this piece is intended to help our members provide effective messaging to their sales personnel.

To view our typical company design/style please see our website at www.kvrtradegroup.org. Our primary RGB colors are: (187,140,9); (94,47,29); (94,138,164); and (164,167,15). Secondary RGB colors are (249,162,28) and (218,210,208). Our title/header font is DIN Next LT Pro and our copy font is Calibri 10.5 pt. We can deviate from the font specification if beneficial.

Target Market(s)

Polystyrene manufacturer plant workers and other employees.

Font styles to use
Sans Serif

Requirements
Must have
• Information presentation must be clean and easy to reference.

```html
<!DOCTYPE html>
<html lang="en">
<head>
<meta charset="utf-8">
<title>EPS Bans – Fact Sheet</title>
<link href="https://fonts.googleapis.com/css2?family=Barlow+Semi+Condensed:ital,wght@0,500;0,600;0,700;1,600;1,700&display=swap" rel="stylesheet">
<style>
  :root {
    --brown: #5e2f1d;
    --gold: #bb8c09;
    --olive: #a4a70f;
    --olive-soft: #e2e2b2;
    --olive-mid: #d4d597;
    --ink: #2a1a12;
    --paper: #ffffff;
  }
  * { margin: 0; padding: 0; box-sizing: border-box; }
  html, body { width: 848px; height: 1200px; overflow: hidden; background: var(--paper); }
  .sheet {
    position: relative; width: 848px; height: 1200px; overflow: hidden;
    font-family: "Barlow Semi Condensed", Arial, sans-serif; color: var(--ink);
  }
  .top-band {
    position: absolute; left: 0; top: 0; width: 848px; height: 47px;
    background: var(--olive);
  }
  .top-band__title {
    position: absolute; right: 28px; top: 13px;
    font-weight: 700; font-size: 21px; color: var(--brown); letter-spacing: .3px;
  }
  .spine {
    position: absolute; left: 14px; top: 47px; width: 20px; height: 1153px;
    background: var(--gold);
  }
  .topic {
    position: absolute; left: 14px; width: 239px;
    background: var(--brown); border-radius: 0 28px 28px 0;
  }
  .topic__title {
    position: absolute; right: 13px; text-align: right;
    color: #fff; font-weight: 600; font-size: 25px; line-height: 33px;
    text-transform: uppercase; letter-spacing: .5px;
  }
  .fact {
    position: absolute; text-align: center; text-transform: uppercase;
    font-weight: 600; font-size: 12.5px; line-height: 15px; color: var(--ink);
  }
  .fact em { font-style: normal; color: var(--gold); }
  .fact .quote { font-style: italic; color: var(--brown); font-weight: 700; }
  .illustration {
    position: absolute; border-radius: 6px;
    background: linear-gradient(180deg, var(--olive-soft), var(--olive-mid));
  }
  .flask { position: absolute; }
  .brand-name {
    position: absolute; left: 0; width: 848px; top: 1052px; text-align: center;
    font-weight: 600; font-size: 28px; color: var(--brown); letter-spacing: .3px;
  }
</style>
</head>
<body>
<div class="sheet">
  <div class="top-band"><span class="top-band__title">EPS BANS</span></div>
  <div class="spine"></div>

  <section class="topic" style="top:68px;height:288px;">
    <h2 class="topic__title" style="top:38px;">There is<br>very little<br>residual<br>styrene in<br>EPS.</h2>
  </section>
  <div class="illustration" role="img" aria-label="Line icon of a steaming coffee cup and a strawberry" style="left:355px;top:100px;width:145px;height:78px;"></div>
  <p class="fact" style="left:315px;top:193px;width:230px;">The <em>amount of styrene</em> that might <em>exist in finished polystyrene is extremely small</em> —often lower than naturally occurring styrene found in everyday food items like coffee, strawberries, and cinnamon.</p>

  <svg class="flask" style="left:660px;top:100px;" width="60" height="80" viewBox="0 0 60 80" aria-hidden="true">
    <g fill="none" stroke="#a4a70f" stroke-width="3" stroke-linejoin="round">
      <path d="M22 4h16M25 4v26L6 72a4 4 0 0 0 4 5h40a4 4 0 0 0 4-5L35 30V4"/>
      <path d="M14 56h32"/>
    </g>
  </svg>
  <p class="fact" style="left:613px;top:193px;width:210px;">All chemicals need to be assessed in terms of risk versus exposure. Risks can be zero, negligible or harmful</p>

  <section class="topic" style="top:377px;height:286px;">
    <h2 class="topic__title" style="top:70px;">EPS is more<br>sustainable<br>than most<br>people<br>imagine</h2>
  </section>
  <div class="illustration" role="img" aria-label="Outlined letters H plus C for hydrogen and carbon" style="left:355px;top:420px;width:135px;height:66px;"></div>
  <p class="fact" style="left:330px;top:527px;width:180px;">Polystyrene is an <em>organic compound</em> consisting of <em>hydrogen and carbon.</em></p>

  <div class="illustration" role="img" aria-label="Plastic resin code 6 recycling symbol" style="left:665px;top:410px;width:84px;height:96px;"></div>
  <p class="fact" style="left:602px;top:527px;width:210px;">Polystyrene is <em>chemically very inert</em>, being <em>resistant to acids and bases</em> but is easily dissolved by many chlorinated solvents, and many aromatic hydrocarbon solvents.</p>

  <section class="topic" style="top:684px;height:308px;">
    <h2 class="topic__title" style="top:99px;">Litter<br>problems<br>are not<br>material<br>dependent</h2>
  </section>
  <div class="illustration" role="img" aria-label="Approval tick icon" style="left:372px;top:720px;width:90px;height:86px;"></div>
  <p class="fact" style="left:308px;top:825px;width:210px;">Polystyrene foam is <em>approved for food contact</em> by the NFSA and other global <em>regulatory agencies</em>.</p>

  <div class="illustration" role="img" aria-label="Line illustration of a sailor hat and debris floating on ocean waves" style="left:647px;top:718px;width:110px;height:104px;"></div>
  <p class="fact" style="left:587px;top:840px;width:230px;">According to the National Ocean &amp; Coast Agency (NOCA), <span class="quote">“Although marine debris is a global issue, there are significant gaps in our understanding of the problem”</span></p>

  <p class="brand-name">KVR Trade Group</p>
</div>
</body>
</html>
```